Innovative psychologist for companies seeks web design for website

Psychologist offers 2 topics:
1. What can a company do to ensure that employees are satisfied and enjoy their work?
The following explanatory video is linked on the website:
https://www.vidplumora.com/watch?v=qTr8ZpLmW3d
2. How can you successfully change your own behavior?
Explanatory video: https://www.vidplumora.com/watch?v=HxK2vQeRt7b&t=6s
The slogan for the second theme will be: YOU are the pirate of your life!

Target Market(s)

companies and private individuals

Number of Pages Required

1 page

Requirements
Nice to have
• Characteristics of the psychologist: pragmatic, down-to-earth, honest, direct, appreciative, enjoys life, loves nature

```html
<!DOCTYPE html>
<html lang="en">
<head>
<meta charset="utf-8">
<title>Lukas Bernhardt – Psychologist</title>
<link rel="stylesheet" href="https://fonts.googleapis.com/css2?family=Playfair+Display+SC:wght@400;700&family=Poppins:wght@300;400;500;600;700&display=swap">
<style>
:root{
  --green:#17990c;
  --dark:#121212;
  --light:#e9e9e5;
  --paper:#f2f2f2;
  --white:#ffffff;
  --ink:#1b1b1b;
  --muted:#3a3a3a;
}
*{margin:0;padding:0;box-sizing:border-box}
html,body{width:1200px;height:3488px;overflow:hidden}
body{font-family:"Poppins",sans-serif;color:var(--ink);background:var(--dark);position:relative}
.section{position:absolute;left:0;width:1200px;overflow:hidden}
.abs{position:absolute}
.display{font-family:"Playfair Display SC",serif;font-weight:400;line-height:1.02}
.btn{position:absolute;display:flex;align-items:center;justify-content:center;border-radius:30px;font-weight:600;font-size:19px;text-decoration:none}
.btn-green{background:var(--green);color:var(--white)}
.btn-dark{background:var(--dark);color:var(--white)}
.copy{font-size:16.5px;line-height:1.28;font-weight:400}

/* hero */
.hero-wrap{top:0;height:674px;background:var(--light)}
.hero{position:absolute;inset:0;border-bottom-right-radius:70px;overflow:hidden;
  background:linear-gradient(180deg,#1d2f4a 0%,#4a5f7a 22%,#c98a52 40%,#6c6a58 55%,#2c3b2a 72%,#1c2a1c 100%)}
.hero-photo{position:absolute;inset:0}
.logo{left:61px;top:38px;color:var(--white);font-weight:700;font-size:19px;line-height:1.4}
.nav{left:348px;top:54px;display:flex;gap:30px;color:var(--white);font-size:18.5px}
.nav-contact{left:915px;top:43px;width:225px;height:44px;border:1.5px solid var(--white);border-radius:24px;color:var(--white);font-size:18.5px;display:flex;align-items:center;justify-content:center}
.hero-title{left:0;width:1200px;top:192px;text-align:center;color:var(--white);font-size:74px;font-weight:700;line-height:1.2}
.hero-sub{left:0;width:1200px;top:466px;text-align:center;color:var(--white);font-size:19px;font-weight:300}
.hero-btn{left:431px;top:519px;width:338px;height:55px;background:#e2e2e2;color:var(--ink)}

/* workplaces */
.work{top:674px;height:509px;background:var(--light)}
.work-photo{left:0;top:0;width:640px;height:509px;background:linear-gradient(90deg,rgba(200,196,186,.55),rgba(233,233,229,.2) 80%,rgba(233,233,229,0))}
.work-title{left:61px;top:64px;font-size:57px;font-weight:700}
.work-copy{left:61px;top:260px;width:480px}
.video-card{background:var(--dark);border-radius:22px;padding:10px}
.video-inner{width:100%;height:100%;border-radius:14px;overflow:hidden;position:relative}
.video-label{position:absolute;left:0;right:0;top:14px;text-align:center;font-weight:600;font-size:19px}
.play{position:absolute;width:46px;height:46px}

/* pirate */
.pirate{top:1183px;height:602px;background:var(--dark)}
.pirate-title{left:623px;top:112px;color:var(--white);font-size:57px;font-weight:700}
.pirate-copy{left:623px;top:313px;width:480px;color:#d8d8d8}

/* psychologist */
.meet{top:1785px;height:594px;background:var(--light)}
.meet-title{left:626px;top:108px;font-size:57px;font-weight:700}
.meet-hello{left:626px;top:252px;font-size:18.5px}
.meet-copy{left:626px;top:298px;width:480px}

/* testimonials */
.clients-wrap{top:2379px;height:593px;background:var(--light)}
.clients{position:absolute;inset:0;background:var(--dark);border-top-left-radius:70px}
.clients-title{left:0;width:1200px;top:56px;text-align:center;color:var(--white);font-size:56px;font-weight:700}
.card{position:absolute;background:var(--white);border-radius:12px;overflow:hidden}
.card-photo{position:absolute;left:9px;right:9px;top:9px;border-radius:6px}
.avatar{position:absolute;border-radius:50%;background:#dcdcdc;display:flex;align-items:center;justify-content:center;font-size:15px;color:#444}
.card-name{position:absolute;font-weight:600;font-size:13px}
.card-copy{position:absolute;text-align:center;font-size:14.5px;line-height:1.3}
.arrow{position:absolute;width:56px;height:56px;border-radius:50%;background:var(--white);box-shadow:0 2px 6px rgba(0,0,0,.3);display:flex;align-items:center;justify-content:center}

/* cta */
.cta{top:2972px;height:402px;background:var(--paper)}
.cta-title{left:0;width:1200px;top:88px;text-align:center;font-size:58px;font-weight:700}
.cta-sub{left:0;width:1200px;top:180px;text-align:center;font-size:18.5px}

.footer{top:3374px;height:114px;background:var(--dark);display:flex;align-items:center;justify-content:center;color:#bdbdbd;font-size:11px}
.footer b{color:var(--white);font-weight:600}
</style>
</head>
<body>

<header class="section hero-wrap">
  <div class="hero">
    <div class="hero-photo" role="img" aria-label="Photo of a man in a beanie looking out over a jungle valley with limestone peaks at sunset"></div>
    <div class="abs logo">Lukas<br>Bernhardt</div>
    <nav class="abs nav"><span>HOME</span><span>ABOUT</span><span>FOR COMPANIES</span><span>FOR INDIVIDUALS</span></nav>
    <div class="abs nav-contact">CONTACT</div>
    <h1 class="abs display hero-title">Transforming Workplaces<br>Empowering Lives</h1>
    <p class="abs hero-sub">Let’s Create Positive Change Together.</p>
    <a class="btn hero-btn">Get in Touch Today →</a>
  </div>
</header>

<section class="section work">
  <div class="abs work-photo" role="img" aria-label="Faded photo of a therapy session in a bright room"></div>
  <svg class="abs" style="left:0;top:0" width="1200" height="509" viewBox="0 0 1200 509">
    <path d="M540 509 C640 380 1000 330 1200 120 L1200 180 C1030 410 720 420 570 509 Z" fill="var(--green)"/>
    <path d="M1200 180 C1030 410 720 420 570 509 L600 509 C740 440 1050 420 1200 210 Z" fill="var(--white)"/>
  </svg>
  <h2 class="abs display work-title">Building<br>Thriving<br>Workplaces.</h2>
  <p class="abs copy work-copy">Lorem Ipsum Dolor Sit Amet, Consectetur Adipiscing Elit. Integer Nec Odio. Praesent Libero. Sed Cursus Ante Dapibus Diam...</p>
  <a class="btn btn-green" style="left:61px;top:393px;width:336px;height:55px">Get in Touch Today →</a>
  <div class="abs video-card" style="left:600px;top:61px;width:486px;height:386px">
    <div class="video-inner" role="img" aria-label="Explainer video thumbnail: sketched chart on a whiteboard and a cartoon office worker at a desk by city windows" style="background:linear-gradient(90deg,#f4f4f4 0%,#efefef 38%,#b9c3cc 39%,#8e9aa6 75%,#c9b79a 100%)">
      <div class="video-label" style="background:var(--white);top:0;padding:10px 0;">Why Employees are Unhappy?</div>
      <svg class="play" style="left:212px;top:170px" viewBox="0 0 46 46"><circle cx="23" cy="23" r="22" fill="#c8141a"/><path d="M18 14 L32 23 L18 32 Z" fill="#fff"/></svg>
    </div>
  </div>
</section>

<section class="section pirate">
  <div class="abs" role="img" aria-label="Faint ship steering wheel decoration" style="left:720px;top:0;width:470px;height:500px;background:radial-gradient(circle at 50% 50%,rgba(90,60,35,.55) 0%,rgba(70,48,30,.35) 40%,rgba(18,18,18,0) 70%)"></div>
  <div class="abs video-card" style="left:65px;top:106px;width:487px;height:387px;background:var(--white)">
    <div class="video-inner" role="img" aria-label="Explainer video thumbnail: cartoon man holding a trophy on a mountain with question marks, caption asking if you want to change your behavior to achieve your goals" style="background:radial-gradient(circle at 50% 62%,#7fb59a 0%,#a8cfc0 30%,#cfcfcf 55%,#d3d3d3 100%)">
      <svg class="play" style="left:209px;top:170px" viewBox="0 0 46 46"><circle cx="23" cy="23" r="22" fill="#c8141a"/><path d="M18 14 L32 23 L18 32 Z" fill="#fff"/></svg>
    </div>
  </div>
  <h2 class="abs display pirate-title">YOU are the<br>pirate of your<br>life!</h2>
  <p class="abs copy pirate-copy">Lorem Ipsum Dolor Sit Amet, Consectetur Adipiscing Elit. Integer Nec Odio. Praesent Libero. Sed Cursus Ante Dapibus Diam...</p>
  <a class="btn btn-green" style="left:623px;top:436px;width:337px;height:56px">Get in Touch Today →</a>
</section>

<section class="section meet">
  <svg class="abs" style="left:0;top:0" width="1200" height="594" viewBox="0 0 1200 594">
    <path d="M0 0 H650 C560 130 320 140 170 180 C60 215 10 280 0 360 Z" fill="var(--dark)"/>
  </svg>
  <div class="abs" role="img" aria-label="Photo of the psychologist seated in conversation with a client in a bright room" style="left:0;top:150px;width:625px;height:444px;background:linear-gradient(90deg,rgba(150,130,110,.8) 0%,rgba(185,175,160,.7) 55%,rgba(233,233,229,0) 100%)"></div>
  <svg class="abs" style="left:0;top:0" width="700" height="594" viewBox="0 0 700 594">
    <path d="M650 0 C560 130 320 140 170 180 C60 215 10 280 0 360 L0 420 C20 300 80 250 200 215 C380 170 560 140 640 20 Z" fill="var(--green)"/>
  </svg>
  <h2 class="abs display meet-title">Meet Your<br>Psychologist</h2>
  <p class="abs meet-hello">Hello I’m Dr. Lukas Bernhardt.</p>
  <p class="abs copy meet-copy">Lorem Ipsum Dolor Sit Amet, Consectetur Adipiscing Elit. Integer Nec Odio. Praesent Libero. Sed Cursus Ante Dapibus Diam...</p>
  <a class="btn btn-green" style="left:626px;top:433px;width:337px;height:55px">Get in Touch with Me →</a>
</section>

<section class="section clients-wrap">
  <div class="clients">
    <h2 class="abs display clients-title">My Previous Clients Say...</h2>

    <div class="card" style="left:115px;top:196px;width:300px;height:316px">
      <div class="card-photo" role="img" aria-label="Landscape photo of waterfalls among green karst hills" style="height:108px;background:linear-gradient(180deg,#9fb8c8,#4f7d4a 60%,#5aa3a0)"></div>
      <div class="avatar" style="left:26px;top:55px;width:84px;height:84px">Photo</div>
      <div class="card-name" style="left:108px;top:122px">Client Name 1</div>
      <p class="card-copy" style="left:12px;width:280px;top:180px">Lorem Ipsum Dolor Sit Amet, Consectetur Adipiscing Elit. Integer Nec Odio. Praesent Libero. Sed Cursus Ante Dapibus Diam...</p>
    </div>

    <div class="card" style="left:780px;top:196px;width:305px;height:316px">
      <div class="card-photo" role="img" aria-label="Landscape photo of misty hills with terraced tea fields" style="height:108px;background:linear-gradient(180deg,#b7b1a2,#6f6a52 55%,#45502e)"></div>
      <div class="avatar" style="left:0;top:55px;width:84px;height:84px">Photo</div>
      <div class="card-name" style="left:80px;top:122px">Client Name 3</div>
      <p class="card-copy" style="left:12px;width:286px;top:160px">Lorem Ipsum Dolor Sit Amet, Consectetur Adipiscing Elit. Integer Nec Odio. Praesent Libero. Sed Cursus Ante Dapibus Diam...</p>
    </div>

    <div class="card" style="left:405px;top:176px;width:375px;height:356px;border-radius:14px">
      <div class="card-photo" role="img" aria-label="Landscape photo of a waterfall cascading through lush forest" style="height:123px;background:linear-gradient(180deg,#a9c3d6,#4e7c3c 50%,#8fbfa8)"></div>
      <div class="avatar" style="left:18px;top:62px;width:94px;height:94px;font-size:17px">Photo</div>
      <div class="card-name" style="left:123px;top:137px;font-size:15px">Client Name 2</div>
      <p class="card-copy" style="left:20px;width:335px;top:183px;font-size:17px">Lorem Ipsum Dolor Sit Amet, Consectetur Adipiscing Elit. Integer Nec Odio. Praesent Libero. Sed Cursus Ante Dapibus Diam...</p>
    </div>

    <div class="arrow" style="left:88px;top:306px"><svg width="24" height="30" viewBox="0 0 24 30"><path d="M17 2 L5 15 L17 28" fill="none" stroke="#111" stroke-width="2.5"/></svg></div>
    <div class="arrow" style="left:1053px;top:306px"><svg width="24" height="30" viewBox="0 0 24 30"><path d="M7 2 L19 15 L7 28" fill="none" stroke="#111" stroke-width="2.5"/></svg></div>
  </div>
</section>

<section class="section cta">
  <h2 class="abs display cta-title">Ready to start your journey?</h2>
  <p class="abs cta-sub">Reach out today!</p>
  <a class="btn btn-green" style="left:252px;top:260px;width:336px;height:55px">For Companies Inquiry →</a>
  <a class="btn btn-dark" style="left:611px;top:260px;width:336px;height:55px">For Individuals Inquiry →</a>
</section>

<footer class="section footer">© 2024&nbsp;<b>Lukas Bernhardt.</b>&nbsp;All Rights Reserved.</footer>

</body>
</html>
```